Builders Worksite Corflute Outdoor Sign

We are a building company who are just branching out into new construction. How first new build is our own home which was designed by us and a local architect. We are proud and want to create more advertisement around our business.

We need a corflute sign that can staked outside the construction site and can be seen by people passing by.
Updates

Can we please make the company name and logo bigger (Tidewater Ridge Homes) This needs to be the focus. Can we please replace 'Manu' with 'Contact Us on 021-574-3619'

Target Market(s)

Home owners and people wishing to build on lifestyle blocks in New Zealand.

Font styles to use
Sans Serif

Requirements
Must have
• It needs to feature our:
Logo
Company name
Contact name and number - Manu - 0215743619
Landscape NOT portrait.

```html
<!DOCTYPE html>
<html lang="en">
<head>
<meta charset="utf-8">
<title>Tidewater Ridge Homes – Site Sign</title>
<link rel="stylesheet" href="https://fonts.googleapis.com/css2?family=Barlow+Semi+Condensed:wght@600;700&display=swap">
<style>
  :root {
    --sign-yellow: #f8d71c;
    --sign-yellow-deep: #f1cc12;
    --sign-navy: #1a1f2e;
    --sign-white: #ffffff;
    --accent-gold: #f2be17;
  }
  * { margin: 0; padding: 0; box-sizing: border-box; }
  html, body {
    width: 1200px;
    height: 896px;
    overflow: hidden;
    background: var(--sign-navy);
  }
  .sign {
    position: relative;
    width: 1200px;
    height: 896px;
    font-family: "Barlow Semi Condensed", "Arial Narrow", sans-serif;
    overflow: hidden;
  }
  .brand-panel {
    position: absolute;
    left: 0; top: 0;
    width: 1200px;
    height: 647px;
    background: linear-gradient(135deg, var(--sign-yellow) 0%, var(--sign-yellow-deep) 45%, var(--sign-yellow) 100%);
  }
  .brand-mark {
    position: absolute;
    left: 60px;
    top: 170px;
    width: 310px;
    height: 310px;
    border-radius: 50%;
    background: var(--sign-navy);
  }
  .brand-name {
    position: absolute;
    left: 420px;
    top: 96px;
    width: 760px;
    color: var(--sign-navy);
    font-weight: 700;
    font-size: 158px;
    line-height: 150px;
    letter-spacing: 1px;
    text-transform: uppercase;
    white-space: nowrap;
  }
  .divider {
    position: absolute;
    left: 0; top: 647px;
    width: 1200px;
    height: 12px;
    background: var(--sign-white);
  }
  .contact-band {
    position: absolute;
    left: 0; top: 659px;
    width: 1200px;
    height: 237px;
    background: var(--sign-navy);
  }
  .contact-tab {
    position: absolute;
    left: 209px;
    top: 647px;
    width: 747px;
    height: 104px;
  }
  .contact-label {
    position: absolute;
    left: 209px;
    top: 664px;
    width: 747px;
    text-align: center;
    color: var(--sign-navy);
    font-weight: 700;
    font-size: 76px;
    line-height: 76px;
    text-transform: uppercase;
  }
  .contact-line {
    position: absolute;
    left: 40px;
    top: 775px;
    display: flex;
    align-items: center;
    gap: 26px;
    font-weight: 700;
    font-size: 116px;
    line-height: 110px;
    white-space: nowrap;
  }
  .contact-name { color: var(--accent-gold); text-transform: uppercase; }
  .phone-icon { width: 82px; height: 82px; flex: none; }
  .contact-number { color: var(--sign-white); letter-spacing: 1px; }
</style>
</head>
<body>
  <div class="sign">
    <div class="brand-panel" role="img" aria-label="Yellow faceted low-poly background texture"></div>
    <div class="brand-mark"></div>
    <h1 class="brand-name">Tidewater<br>Ridge<br>Homes</h1>

    <div class="divider"></div>
    <div class="contact-band"></div>
    <svg class="contact-tab" viewBox="0 0 747 104" aria-hidden="true">
      <path d="M0 0 H747 L700 78 Q685 104 650 104 H97 Q62 104 47 78 Z" fill="#ffffff"/>
    </svg>
    <p class="contact-label">Contact us on</p>

    <p class="contact-line">
      <span class="contact-name">Manu</span>
      <svg class="phone-icon" viewBox="0 0 82 82" aria-hidden="true">
        <circle cx="41" cy="41" r="36" fill="none" stroke="#f2be17" stroke-width="6"/>
        <path d="M33 22 q-8 3 -8 14 q2 16 18 26 q8 4 13 -2 l2 -4 l-8 -7 l-5 4 q-8 -5 -11 -14 l4 -4 l-4 -11 z" fill="#f2be17"/>
      </svg>
      <span class="contact-number">021-574-3619</span>
    </p>
  </div>
</body>
</html>
```